Ferncastle Financial - Website Design

We need a website design for a new commercial real estate company called Ferncastle Financial. We're effectively commercial mortgage brokers connecting real estate investors to lenders. We need a website that is simple (not busy), elegant, professional, and user-friendly. A lot of the users will be in their 50's and less tech savvy, so a stream-lined design is best. The website will serve as a portal for lenders to review new financing opportunities, as well as for real estate investors to review terms from lenders.
Updates
Just uploaded our logo.
Target Market(s)
Commercial real estate investors and lenders
Industry/Entity Type
Real Estate
Number of Pages Required
1 page
Colors
Designer to choose colors to be used in the design.
Look and feel

```html
<!DOCTYPE html>
<html lang="en">
<head>
<meta charset="utf-8">
<title>Ferncastle Financial</title>
<link href="https://fonts.googleapis.com/css2?family=Roboto:wght@400;500;700&display=swap" rel="stylesheet">
<style>
:root{
  --blue:#1d4fcc;
  --sky:#1e84c4;
  --link:#1f56c9;
  --text:#6f6f6f;
  --heading:#4f4f4f;
  --card:#f3f3f3;
  --magenta:#c2256e;
  --olive:#8f9a4a;
  --gold:#e0ab2a;
  --red:#d9221c;
}
*{margin:0;padding:0;box-sizing:border-box}
html,body{width:864px;height:1200px;overflow:hidden;background:#fff}
body{position:relative;font-family:'Roboto',Arial,sans-serif;color:var(--text)}
.abs{position:absolute}
/* header */
.site-header{position:absolute;left:0;top:0;width:864px;height:56px;border-bottom:2px solid var(--blue);background:#fff}
.brand{left:112px;top:14px;display:flex;align-items:center;gap:6px;font-size:16px;font-weight:500;color:var(--link);letter-spacing:.5px}
.brand .dot{width:12px;height:12px;background:var(--link)}
.nav{left:298px;top:37px;display:flex;gap:23px;font-size:9.5px;color:#8a8a8a;letter-spacing:.2px}
.nav .active{color:var(--link)}
.advisor{left:669px;top:26px;font-size:7px;color:#9a9a9a}
.advisor b{display:block;font-size:10px;font-weight:500;color:var(--link);letter-spacing:.5px;margin-top:3px}
/* hero */
.hero{left:0;top:56px;width:864px;height:246px;background:linear-gradient(180deg,#2f7fe0 0%,#6aa6ec 45%,#8a9aa8 70%,#27538f 100%)}
.hero-title{left:112px;top:92px;font-size:25px;font-weight:700;color:#fff}
.hero-sub{left:112px;top:144px;font-size:18px;font-weight:500;color:#fff;line-height:19px}
/* login panels */
.login{top:276px;width:316px;height:124px;color:#fff}
.login.investors{left:110px;background:var(--sky)}
.login.lenders{left:436px;background:var(--blue)}
.login h2{position:absolute;top:14px;font-size:9px;font-weight:500;letter-spacing:.3px}
.login p{position:absolute;top:42px;width:186px;font-size:7.8px;line-height:9.3px}
.login .btn{position:absolute;top:85px;width:103px;height:22px;background:#fff;border-radius:2px;color:var(--link);font-size:9px;font-weight:500;display:flex;align-items:center;justify-content:center}
.login svg{position:absolute}
/* action row */
.actions{left:0;top:400px;width:864px;height:53px;border-bottom:2px solid #e2e2e2}
.action{position:absolute;top:0;height:51px;display:flex;align-items:center;gap:12px;font-size:10.5px;color:var(--link)}
/* welcome */
.welcome h1{left:112px;top:498px;font-size:18.5px;font-weight:500;color:var(--heading)}
.welcome p{position:absolute;left:112px;width:378px;font-size:7.6px;line-height:9.3px}
.video{left:515px;top:499px;width:236px;height:140px;border:1px solid #ddd;padding:3px}
.video .inner{width:100%;height:100%;background:#e6e6e6;text-align:center;position:relative}
.video .label{padding-top:14px;font-size:8px;color:#555}
.video .caption{margin-top:7px;font-size:8px;line-height:12px;color:#2a7fd4;font-weight:500}
.video .play{position:absolute;left:103px;top:64px;width:32px;height:24px;background:var(--red);border-radius:6px}
.video .name{position:absolute;left:0;right:0;top:108px;font-size:7px;color:var(--link);font-weight:500}
/* cards */
.card{top:682px;width:206px;height:255px;background:var(--card);overflow:hidden}
.card h3{position:absolute;left:15px;top:15px;width:176px;font-size:10.2px;font-weight:500;color:var(--heading);padding-bottom:5px;border-bottom:2px solid}
.card ul{position:absolute;left:17px;top:42px;list-style:none;font-size:7.8px;line-height:12.5px}
.card li::before{content:"•";margin-right:6px}
.card p{position:absolute;left:16px;width:184px;font-size:7.7px;line-height:9.3px}
.card .more{position:absolute;right:0;bottom:0;width:37px;height:37px}
.card .more span{position:absolute;right:6px;bottom:3px;font-size:7px;color:#fff}
.c1 h3{border-color:var(--magenta)} .c1 li::before{color:var(--magenta)}
.c2 h3{border-color:var(--olive)} .c2 li::before{color:var(--olive)}
.c3 h3{border-color:var(--gold)} .c3 li::before{color:var(--gold)}
/* footer */
.site-footer{left:0;top:983px;width:864px;height:217px;background:var(--blue);color:#fff}
.foot-brand{position:absolute;left:118px;top:42px;display:flex;align-items:center;gap:6px;font-size:16px;font-weight:500;letter-spacing:.5px}
.foot-brand .dot{width:12px;height:12px;background:#fff}
.foot-call{position:absolute;left:156px;top:85px;font-size:8px}
.foot-call b{font-size:9.5px;font-weight:500;margin-left:6px;letter-spacing:.4px}
.foot-links{position:absolute;left:338px;top:45px;list-style:none;font-size:8px;font-weight:500;line-height:18.7px}
.newsletter{position:absolute;left:538px;top:44px;font-size:8px;font-weight:500}
.signup{position:absolute;left:538px;top:66px;display:flex}
.signup .field{width:137px;height:24px;background:#fff;color:#aaa;font-size:7.5px;padding:8px 6px}
.signup .go{width:61px;height:24px;background:var(--gold);font-size:8px;font-weight:700;display:flex;align-items:center;justify-content:center}
.copyright{position:absolute;left:0;width:864px;top:195px;text-align:center;font-size:7px;font-weight:500}
</style>
</head>
<body>

<header class="site-header">
  <div class="abs brand"><span class="dot"></span>FERNCASTLE FINANCIAL</div>
  <nav class="abs nav"><span class="active">HOME</span><span>SOLUTIONS</span><span>PORTFOLIO</span><span>COMPANY</span><span>CONTACT US</span></nav>
  <div class="abs advisor">Speak to an Advisor<b>012 55501234</b></div>
</header>

<div class="abs hero" role="img" aria-label="Photograph of a city skyline across the water under a blue sky"></div>
<div class="abs hero-title">Ferncastle Financial</div>
<div class="abs hero-sub">We are connecting real estate<br>investors to lenders</div>

<section class="abs login investors">
  <svg style="left:25px;top:36px" width="54" height="48" viewBox="0 0 54 48" fill="none" stroke="#fff" stroke-width="2.5">
    <path d="M2 46h50"/><rect x="5" y="34" width="6" height="10"/><rect x="15" y="28" width="6" height="16"/><rect x="25" y="22" width="6" height="22"/><rect x="35" y="14" width="6" height="30"/>
    <path d="M3 30 18 18l10 6L46 4"/><path d="M38 4h9v9"/>
  </svg>
  <h2 style="left:104px">INVESTORS LOGIN</h2>
  <p style="left:104px">We are excited and honored to be your financing partner for one of the most important and exciting milestones in your life.</p>
  <div class="btn" style="left:104px">LOGIN</div>
</section>

<section class="abs login lenders">
  <svg style="left:26px;top:32px" width="56" height="52" viewBox="0 0 56 52" fill="none" stroke="#fff" stroke-width="2">
    <path d="M4 22 24 4l20 18"/><path d="M9 18v24h16"/><path d="M39 18v6"/>
    <ellipse cx="42" cy="30" rx="10" ry="4"/><path d="M32 30v14c0 2 4.5 4 10 4s10-2 10-4V30"/><path d="M32 37c0 2 4.5 4 10 4s10-2 10-4"/>
    <ellipse cx="28" cy="38" rx="7" ry="3"/><path d="M21 38v8c0 1.5 3 3 7 3"/>
  </svg>
  <h2 style="left:112px">LENDERS LOGIN</h2>
  <p style="left:112px">Use our origination strategy to write more business as a lender and be part of the conversation with high quality borrowers</p>
  <div class="btn" style="left:111px">LOGIN</div>
</section>

<div class="abs actions">
  <div class="action" style="left:131px">
    <svg width="26" height="24" viewBox="0 0 26 24" fill="none" stroke="#555" stroke-width="1.6"><path d="M11 2C5 2 1 5.5 1 10c0 2.5 1 4.5 3 6l-1 5 5-3c1 .3 2 .4 3 .4"/><circle cx="18" cy="16" r="7"/><circle cx="15" cy="16" r=".6" fill="#555"/><circle cx="18" cy="16" r=".6" fill="#555"/><circle cx="21" cy="16" r=".6" fill="#555"/></svg>
    Request Info
  </div>
  <svg class="abs" style="left:292px;top:6px" width="22" height="40" viewBox="0 0 22 40" fill="none" stroke="#cfcfcf" stroke-width="1.2"><path d="M1 1l20 19L1 39"/></svg>
  <div class="action" style="left:381px">
    <svg width="22" height="24" viewBox="0 0 22 24" fill="none" stroke="#555" stroke-width="1.5"><path d="M16 8V1H1v22h15v-3"/><path d="M4 6h9M4 10h9M4 14h6M4 18h5"/><path d="M20 8 12 18l-1 3 3-1 8-10z"/></svg>
    Submit a Loan
  </div>
  <svg class="abs" style="left:538px;top:6px" width="22" height="40" viewBox="0 0 22 40" fill="none" stroke="#cfcfcf" stroke-width="1.2"><path d="M1 1l20 19L1 39"/></svg>
  <div class="action" style="left:609px">
    <svg width="22" height="22" viewBox="0 0 22 22"><path d="M4 1l4 5-2 3c1.5 3 4 5.5 7 7l3-2 5 4-2 3C11 21 1 11 1 3z" fill="#555"/></svg>
    <span style="margin-left:8px">Request a Call Back</span>
  </div>
</div>

<section class="welcome">
  <h1 class="abs">Welcome to Ferncastle Financial</h1>
  <p style="top:541px">Sed ut perspiciatis unde omnis iste natus error sit voluptatem accusantium doloremque laudantium, totam rem aperiam, eaque ipsa quae ab illo inventore veritatis et quasi architecto beatae vitae dicta sunt explicabo. Nemo enim ipsam voluptatem quia voluptas sit aspernatur aut odit aut fugit, sed quia consequuntur magni dolores eos qui ratione voluptatem sequi nesciunt. Neque porro quisquam est, qui dolorem ipsum quia dolor sit amet, consectetur, adipisci velit, sed quia non numquam eius modi tempora incidunt ut labore et dolore magnam aliquam quaerat voluptatem.</p>
  <p style="top:606px">Sed ut perspiciatis unde omnis iste natus error sit voluptatem accusantium doloremque laudantium, totam rem aperiam, eaque ipsa quae ab illo inventore veritatis et quasi architecto beatae vitae dicta sunt explicabo.</p>
  <div class="abs video">
    <div class="inner">
      <div class="label">WATCH VIDEO</div>
      <div class="caption">INTRODUCTION TO INVESTING AT<br>FERNCASTLE FINANCIAL</div>
      <div class="play"><svg width="32" height="24" viewBox="0 0 32 24"><path d="M13 8v8l7-4z" fill="#fff"/></svg></div>
      <div class="name">FERNCASTLE FINANCIAL</div>
    </div>
  </div>
</section>

<article class="abs card c1" style="left:112px">
  <h3>Commercial Mortgages</h3>
  <ul><li>Working with us</li><li>Our team</li><li>Mortgage solutions</li><li>Resources and insights</li><li>Recent financing</li></ul>
  <p style="top:116px">Whether you are looking to acquire a new commercial real estate property or refinance an existing one, you can look to Northgate National as your advisor. We deliver value beyond the loans with our spirit to take smart risks, deep expertise, broad product portfolio, diverse specialists and commitment to quick execution and responsiveness. Our commercial business spans the spectrum of properties from multi-family residential, retail, office, industrial, seniors housing to self-storage and hotels.</p>
  <div class="more"><svg width="37" height="37"><path d="M37 0v37H0z" fill="var(--magenta)"/></svg><span>More</span></div>
</article>

<article class="abs card c2" style="left:325px">
  <h3>Residential Mortgages</h3>
  <ul><li>Managing your mortgage</li><li>Pay down your mortgage faster</li><li>Mortgage calculators</li><li>Mortgage rates</li></ul>
  <p style="top:116px">We are excited and honored to be your financing partner for one of the most important and exciting milestones in your life.</p>
  <div class="more"><svg width="37" height="37"><path d="M37 0v37H0z" fill="var(--olive)"/></svg><span>More</span></div>
</article>

<article class="abs card c3" style="left:538px">
  <h3>Mortgage Brokers</h3>
  <ul><li>Northgate National difference</li><li>Our team</li><li>Resources for Mortgage Brokers</li><li>Mortgage solutions</li></ul>
  <p style="top:116px">For most lenders, service means good rates, deals that close and quick turnaround time. For us, executing efficiently is just how we do business. But service, real service, is much more.</p>
  <div class="more"><svg width="37" height="37"><path d="M37 0v37H0z" fill="var(--gold)"/></svg><span>More</span></div>
</article>

<footer class="abs site-footer">
  <div class="foot-brand"><span class="dot"></span>FERNCASTLE FINANCIAL</div>
  <div class="foot-call">Call<b>012 55501234</b></div>
  <ul class="foot-links">
    <li>About Ferncastle Financial</li><li>Our Products</li><li>Contact Us</li><li>Become an Introducer</li><li>Sitemap</li><li>Terms of Use</li><li>Privacy &amp; Cookie Policy</li>
  </ul>
  <div class="newsletter">Subscribe Newsletter</div>
  <div class="signup"><div class="field">Enter your email address</div><div class="go">SUBSCRIBE</div></div>
  <div class="copyright">Copyright © 2017 FerncastleFinancial</div>
</footer>

</body>
</html>
```